Business card for STEADYWAVE

Please design professional business card for IT consulting firm STEADYWAVE INC.
Use logo attached.
Use information from sample qNode business card attached.
replace qnode inc with STEADYWAVE INC.
as well as qnodeinc.com with steadywave.example

```html
<!DOCTYPE html>
<html lang="en">
<head>
<meta charset="utf-8">
<title>STEADYWAVE Business Card</title>
<link rel="stylesheet" href="https://fonts.googleapis.com/css2?family=Outfit:wght@300;400;700&display=swap">
<style>
  :root {
    --backdrop: #e4e4e2;
    --card-white: #ffffff;
    --card-black: #020303;
    --ink: #111111;
    --accent-purple: #6e3b96;
    --rule-purple: #6e3b96;
  }
  * { margin: 0; padding: 0; box-sizing: border-box; }
  html, body {
    width: 1200px;
    height: 846px;
    overflow: hidden;
  }
  body {
    background: var(--backdrop);
    font-family: "Outfit", sans-serif;
    color: var(--ink);
    position: relative;
  }
  .card {
    position: absolute;
    left: 347px;
    width: 509px;
    height: 291px;
  }
  .card--front { top: 99px; background: var(--card-white); }
  .card--back { top: 457px; background: var(--card-black); }

  .wordmark {
    position: absolute;
    display: flex;
    align-items: center;
    gap: 10px;
    font-family: "Outfit", sans-serif;
    font-weight: 700;
    letter-spacing: 0.08em;
    line-height: 1;
    white-space: nowrap;
  }
  .wordmark__square {
    width: 0.28em;
    height: 0.28em;
    background: var(--accent-purple);
  }
  .card--front .wordmark {
    left: 29px;
    top: 63px;
    font-size: 34px;
    color: var(--ink);
  }
  .card--back .wordmark {
    left: 50%;
    top: 50%;
    transform: translate(-50%, -50%);
    font-size: 50px;
    color: var(--card-white);
  }

  .role {
    position: absolute;
    left: 29px;
    top: 130px;
    font-size: 14px;
    font-weight: 300;
    letter-spacing: 0.01em;
    text-transform: uppercase;
  }
  .person {
    position: absolute;
    left: 29px;
    top: 150px;
    font-size: 16px;
    font-weight: 700;
    color: var(--accent-purple);
    text-transform: uppercase;
  }
  .person__credential { font-size: 10px; }

  .contact {
    position: absolute;
    top: 186px;
    font-size: 14.5px;
    font-weight: 300;
    line-height: 19px;
    white-space: nowrap;
  }
  .contact--phones { left: 29px; }
  .contact--web { left: 248px; }
  .contact__label {
    font-weight: 700;
    color: var(--accent-purple);
  }

  .divider-rule {
    position: absolute;
    left: 0;
    top: 240px;
    width: 100%;
    height: 8px;
    background: var(--rule-purple);
  }
  .address {
    position: absolute;
    left: 29px;
    top: 260px;
    font-size: 14.5px;
    font-weight: 400;
    letter-spacing: 0.01em;
    white-space: nowrap;
  }
</style>
</head>
<body>
  <section class="card card--front" aria-label="Business card front">
    <div class="wordmark"><span>STEADYWAVE</span><span class="wordmark__square"></span></div>

    <p class="role">General Manager</p>
    <p class="person">Daniel Moreau, <span class="person__credential">P. Eng.</span></p>

    <div class="contact contact--phones">
      <p><span class="contact__label">office:</span> (555) 310-4820 ext. 201</p>
      <p><span class="contact__label">mobile:</span> (555) 742-1906</p>
    </div>
    <div class="contact contact--web">
      <p><span class="contact__label">email:</span> dmoreau@steadywave.example</p>
      <p><span class="contact__label">www.steadywave.example</span></p>
    </div>

    <div class="divider-rule"></div>
    <p class="address">1280 Harbourline Rd., Suite 101 Lakeview, Ontario, A1B 2C3, Canada</p>
  </section>

  <section class="card card--back" aria-label="Business card back">
    <div class="wordmark"><span>STEADYWAVE</span><span class="wordmark__square"></span></div>
  </section>
</body>
</html>
```